Postcard Design

Law office.
Details are on the attached pdf file:
NOTE: the following items are to be changed, as follows:
1. price is 799
2. delete "Expires 2-8-13"
3. make "Nevada County's..." into "Northern California's ... "
4. Someplace where it fits nicely, add "Fast, Easy, Done!"
5. Delete "no obligation first visit"
6. That attached pdf was a successful ad so I want to maintain that look GENERALLY, but I'm not stuck on anything in particular. Some freedom to play with it for a perfect ad.
7. I'll attach the revised picture and the logo.

```html
<!DOCTYPE html>
<html lang="en">
<head>
<meta charset="utf-8">
<title>Law Office Of Daniel R. Moreno — Estate Plans Postcard</title>
<link rel="stylesheet" href="https://fonts.googleapis.com/css2?family=EB+Garamond:ital,wght@0,400;0,600;0,700;1,400;1,600;1,700&display=swap">
<style>
  :root {
    --ink: #231f20;
    --bg-light: #e6e6e6;
    --bg-mid: #cfcfcf;
    --bg-dark: #a9a9a9;
    --photo-top: #6b6b6b;
    --photo-bottom: #1e1e1e;
  }
  * { margin: 0; padding: 0; box-sizing: border-box; }
  html, body { width: 1200px; height: 862px; overflow: hidden; }
  body { font-family: "EB Garamond", Georgia, serif; color: var(--ink); }
  .postcard {
    position: relative;
    width: 1200px; height: 862px; overflow: hidden;
    background: radial-gradient(ellipse at 50% 45%, var(--bg-light) 0%, var(--bg-mid) 55%, var(--bg-dark) 100%);
  }
  .postcard > * { position: absolute; line-height: 1; white-space: nowrap; }
  .headline {
    top: 52px; left: 0; width: 1200px; text-align: center;
    font-size: 52px; font-weight: 700; letter-spacing: -1.6px;
  }
  .services {
    top: 134px; left: 0; width: 1200px; text-align: center;
    font-size: 45px; font-style: italic; letter-spacing: 0.6px;
  }
  .price {
    top: 226px; left: 206px;
    font-size: 150px; font-weight: 600; letter-spacing: -2px;
  }
  .value {
    top: 260px; left: 673px;
    font-size: 26px; font-weight: 700; letter-spacing: 0.6px;
  }
  .tagline {
    top: 302px; left: 673px;
    font-size: 33px; font-weight: 700;
  }
  .protect {
    top: 402px; left: 0; width: 1200px; text-align: center;
    font-size: 58px; font-weight: 700; padding-right: 2px;
  }
  .call-now {
    top: 474px; left: 398px;
    font-size: 32px; font-weight: 700;
  }
  .attorney-photo { left: 36px; top: 464px; width: 300px; height: 398px; }
  .office-label {
    top: 562px; left: 459px;
    font-size: 32px; font-weight: 400;
  }
  .office-name {
    top: 600px; left: 312px; width: 700px; text-align: center;
    font-size: 78px; font-weight: 400; letter-spacing: 0.5px;
  }
  .phone {
    top: 732px; left: 462px; width: 400px; text-align: center;
    font-size: 36px; font-weight: 700; letter-spacing: 1px;
  }
  .website {
    top: 771px; left: 362px; width: 600px; text-align: center;
    font-size: 26px; font-weight: 700; font-style: italic;
  }
  .notary {
    top: 806px; left: 462px; width: 400px; text-align: center;
    font-size: 24px;
  }
  .brand-mark {
    top: 598px; left: 1040px; width: 136px; height: 174px;
    border: 3px solid var(--ink);
    display: flex; align-items: center; justify-content: center;
    font-size: 30px; font-weight: 600;
  }
  .since {
    top: 789px; left: 1040px; width: 136px; text-align: center;
    font-size: 16px; font-style: italic; line-height: 1.3;
  }
</style>
</head>
<body>
<main class="postcard">
  <h1 class="headline">Northern California's Best in Estate Plans</h1>
  <p class="services">Living Trusts, Wills &amp; All Necessary Documents</p>

  <p class="price">$799</p>
  <p class="value">OVER $2,000 VALUE</p>
  <p class="tagline">Fast, Easy, Done!</p>

  <h2 class="protect">Protect Your Loved Ones!</h2>
  <p class="call-now">It’s Easy — Call Now!</p>

  <svg class="attorney-photo" viewBox="0 0 300 398" role="img" aria-label="Portrait photo of the attorney in a dark suit and tie">
    <defs>
      <linearGradient id="photoTone" x1="0" y1="0" x2="0" y2="1">
        <stop offset="0" stop-color="var(--photo-top)"/>
        <stop offset="1" stop-color="var(--photo-bottom)"/>
      </linearGradient>
    </defs>
    <rect x="0" y="0" width="300" height="398" rx="40" fill="url(#photoTone)"/>
  </svg>

  <p class="office-label">Law Office Of</p>
  <p class="office-name">Daniel R. Moreno</p>

  <p class="phone">555-0147</p>
  <p class="website">Check me out at: www.DanielMoreno.com</p>
  <p class="notary">Free Notarization</p>

  <div class="brand-mark">Moreno</div>
  <p class="since">Thousands Served<br>Since 1998</p>
</main>
</body>
</html>
```